NEW Modern Sleek Business Card for VR Language Startup

Our startup is using VR to lead the next wave of world language education. We need a two-sided business card that introduces the larger organization (Quorvel Language Inc) and our contact info on one side and shows the product, Lumidrasca, on the other side.

Side 1 (contact info)= Quorvel Logo and Contact info (name, title, phone, email)

Side 2 (product)= Lumidrasc logo, text, and website
Text= Culturally Immersive Language Learning Games
Website= www.lumidrasc.example

Target Market(s)

Education, Technology

Contact Information for Business Card

Contact info will be updated upon approval of the design. For now, put this as a placeholder.

Perry Hollins
Founder & CEO
phollins@mailtrove.example
(555)-014-2736

Font styles to use
Other font styles liked:
• Gibson and Century Gothic are the brand fonts

Requirements
Nice to have
• I would love to see cohesion between the design and colors of the two logos. I have attached a few business card designs that I like, so you can get a feel for my preferred style.

```html
<!DOCTYPE html>
<html lang="en">
<head>
<meta charset="utf-8">
<title>Lumidrasc and Quorvel business card</title>
<link rel="stylesheet" href="https://fonts.googleapis.com/css2?family=Montserrat:ital,wght@0,400;0,500;0,700;1,500&family=Questrial&display=swap">
<style>
  :root {
    --backdrop: #e4e5e8;
    --card-white: #ffffff;
    --card-dark: #1c1f25;
    --pattern-dark: #222a30;
    --ink: #1a1a1a;
    --ink-soft: #555a60;
    --wave-orange: #ff7a2f;
    --wave-red: #f5323f;
    --wave-purple: #7a4dff;
    --accent-blue: #3f7bff;
    --accent-cyan: #2fd3f0;
    --text-light: #f2f4f7;
  }
  * { box-sizing: border-box; margin: 0; padding: 0; }
  html, body { width: 1200px; height: 800px; overflow: hidden; }
  body {
    background: var(--backdrop);
    display: flex;
    align-items: center;
    justify-content: center;
    gap: 40px;
    font-family: "Montserrat", sans-serif;
  }
  .card {
    position: relative;
    width: 540px;
    height: 310px;
    border-radius: 4px;
    overflow: hidden;
    box-shadow: 0 14px 30px rgba(0,0,0,0.18), 0 2px 6px rgba(0,0,0,0.10);
  }

  /* Product side */
  .card--product { background: var(--card-dark); color: var(--text-light); }
  .product-pattern {
    position: absolute; inset: 0;
    background: radial-gradient(ellipse at 60% 40%, var(--pattern-dark), var(--card-dark) 75%);
  }
  .product-brand {
    position: absolute; left: 0; right: 0; top: 96px;
    display: flex; align-items: center; justify-content: center; gap: 12px;
  }
  .brand-dot {
    width: 34px; height: 34px; border-radius: 50%;
    background: var(--accent-blue);
  }
  .brand-name {
    font-family: "Montserrat", sans-serif;
    font-weight: 500;
    font-size: 38px;
    letter-spacing: 0.5px;
    color: var(--text-light);
  }
  .product-rule {
    position: absolute; left: 40px; right: 40px;
    height: 12px;
  }
  .product-rule--top { top: 168px; }
  .product-rule--bottom { top: 228px; }
  .product-tagline {
    position: absolute; left: 0; right: 0; top: 186px;
    text-align: center;
    font-style: italic; font-weight: 500; font-size: 16px;
    color: var(--text-light);
  }
  .product-web {
    position: absolute; left: 0; right: 0; top: 208px;
    text-align: center;
    font-size: 13px; color: #cfd5de;
  }

  /* Contact side */
  .card--contact { background: var(--card-white); color: var(--ink); }
  .contact-wave { position: absolute; inset: 0; }
  .contact-person {
    position: absolute; right: 34px; top: 66px;
    text-align: right; color: #fff;
  }
  .person-name { font-weight: 700; font-size: 22px; }
  .person-title { font-size: 13px; font-weight: 500; margin-top: 2px; }
  .company-brand {
    position: absolute; left: 40px; top: 120px;
    display: flex; align-items: center; gap: 10px;
  }
  .company-brand .brand-name { color: var(--ink); font-size: 32px; font-weight: 700; letter-spacing: 2px; }
  .company-brand .brand-dot { width: 26px; height: 26px; background: var(--wave-red); }
  .contact-details {
    position: absolute; left: 40px; top: 176px;
    font-family: "Questrial", sans-serif;
    font-size: 13px; line-height: 1.6; color: var(--ink-soft);
  }
</style>
</head>
<body>

  <section class="card card--product" aria-label="Product side">
    <div class="product-pattern" role="img" aria-label="Repeating faint brand pattern on dark background"></div>
    <div class="product-brand">
      <span class="brand-dot"></span>
      <span class="brand-name">Lumidrasc</span>
    </div>
    <svg class="product-rule product-rule--top" viewBox="0 0 460 12" preserveAspectRatio="none">
      <line x1="0" y1="6" x2="200" y2="6" stroke="var(--accent-blue)" stroke-width="1.2"/>
      <circle cx="204" cy="6" r="3.5" fill="none" stroke="var(--accent-blue)" stroke-width="1.4"/>
    </svg>
    <p class="product-tagline">Culturally Immersive Language Learning Games</p>
    <p class="product-web">www.lumidrasc.example</p>
    <svg class="product-rule product-rule--bottom" viewBox="0 0 460 12" preserveAspectRatio="none">
      <circle cx="256" cy="6" r="3.5" fill="none" stroke="var(--accent-blue)" stroke-width="1.4"/>
      <line x1="260" y1="6" x2="460" y2="6" stroke="var(--accent-blue)" stroke-width="1.2"/>
    </svg>
  </section>

  <section class="card card--contact" aria-label="Contact side">
    <svg class="contact-wave" viewBox="0 0 540 310" preserveAspectRatio="none">
      <defs>
        <linearGradient id="waveFill" x1="0" y1="1" x2="1" y2="0">
          <stop offset="0" stop-color="var(--wave-purple)"/>
          <stop offset="0.35" stop-color="var(--wave-red)"/>
          <stop offset="1" stop-color="var(--wave-orange)"/>
        </linearGradient>
      </defs>
      <path d="M0,0 H540 V250 C480,244 430,200 380,138 C330,76 280,44 200,42 C120,40 60,52 0,84 Z" fill="url(#waveFill)"/>
      <path d="M0,100 C60,66 120,56 200,58 C280,60 330,92 380,152 C430,214 480,258 540,264" fill="none" stroke="var(--wave-purple)" stroke-width="6"/>
      <path d="M0,92 C60,58 120,48 200,50 C280,52 330,84 380,145 C430,206 480,252 540,257" fill="none" stroke="#fff" stroke-width="3"/>
    </svg>
    <div class="contact-person">
      <p class="person-name">Perry Hollins</p>
      <p class="person-title">Founder &amp; CEO</p>
    </div>
    <div class="company-brand">
      <span class="brand-name">Quorvel</span>
      <span class="brand-dot"></span>
    </div>
    <div class="contact-details">
      <p>P: (555)-014-2736</p>
      <p>phollins@mailtrove.example</p>
    </div>
  </section>

</body>
</html>
```